Jackpot Display Wallpaper Design

We develop Jackpot Systems for Casinos and have a web based Jackpot Odometer display. Our software works by superimposing dynamic content over a fixed background.

We require the design of a fixed background of dimensions 1920 x 1080 incorporating higher quality graphical design work and creative ideas.

See File 4 below - "High Hand TEMPLATE". The finished work will resemble this image, with the grey background replaced with your creative design. The black panels will be replaced with your panels, with nice borders and interior shading or pattern. Our software will dynamically superimpose content over the panels. The panels should be of similar size and location to those shown although this is not strictly rigid and you can relocate or resize panels to a limited extent.

The end result when our software runs is something like File 5 below - "High Hand SAMPLE RESULT". Note that the example shows a patterned blue background, a red logo area, and grey shading within the panels.

The text within the panels is rendered dynamically by our application.

** This is a very plain design and only intended to illustrate how we superimpose text and playing cards onto a background. Do not take any design cues from this image.

Please provide the background, and blank panels. The panels can (and should) have some texture or shading that will look good when we render text over them.

Feel free to suggest a font and/or text color that you think would look good against your background and we can render the content in the font / color you suggest.

Target Market(s)

Poker Room facilities and Casinos

Industry/Entity Type

Software

Font styles to use
Sans Serif

Requirements
Must have
• - A graphic design based on the template called High Hand TEMPLATE.
• - 1920 x 1080 Photoshop image using separate layers.
• - The design needs to be edgy and reflect gaming, casinos and poker rooms.
Nice to have
• -Please see files 1, 2, and 3 below by way of "edgy" style guide.
• - For files 1, 2, 3 - ignore the "Bad Beat" wording but focus on the design style by way of example.
• - The background may or may not include the words "Poker" and / or "Jackpot"
• - You can fill in the panels with some sample content to illustrate how it will look.
• - The area at bottom containing scrolling text may be a frame with a border or just an area where we superimpose the scrolling text.

```html
<!DOCTYPE html>
<html lang="en">
<head>
<meta charset="utf-8">
<title>High Hand Bonus Display</title>
<link href="https://fonts.googleapis.com/css2?family=Montserrat:wght@500;600;700;800&display=swap" rel="stylesheet">
<style>
  :root {
    --bg-red: #990000;
    --panel-black: #0a0a0a;
    --panel-dark: #1c1c1c;
    --chrome-light: #f4f4f4;
    --chrome-mid: #a9a9a9;
    --chrome-dark: #5a5a5a;
    --text-white: #ffffff;
    --card-white: #ffffff;
    --card-edge: #bdbdbd;
    --suit-red: #e3191b;
    --suit-black: #111111;
  }
  * { box-sizing: border-box; margin: 0; padding: 0; }
  html, body {
    width: 1200px; height: 1000px; overflow: hidden;
    background: var(--bg-red);
    font-family: "Montserrat", Arial, sans-serif;
  }
  .canvas { position: relative; width: 1200px; height: 1000px; background: var(--bg-red); }

  .chrome {
    position: absolute;
    background: linear-gradient(180deg, var(--chrome-light) 0%, var(--chrome-mid) 45%, var(--chrome-dark) 55%, var(--chrome-light) 100%);
    box-shadow: 0 2px 4px rgba(0,0,0,.45);
  }
  .title-tab { left: 422px; top: 418px; width: 356px; height: 46px; border-radius: 9px 9px 0 0; }
  .title-tab .inner {
    position: absolute; left: 5px; top: 5px; right: 5px; bottom: 0;
    border-radius: 6px 6px 0 0;
    background: linear-gradient(180deg, #3a3a3a 0%, var(--panel-black) 55%, #000 100%);
    display: flex; align-items: center; justify-content: center;
  }
  .title {
    color: var(--text-white); font-weight: 800; font-size: 24px; letter-spacing: .5px;
    text-shadow: 0 1px 2px rgba(0,0,0,.8);
  }

  .main-bar { left: 282px; top: 456px; width: 636px; height: 125px; border-radius: 9px; }

  .panel {
    position: absolute; top: 6px; bottom: 7px;
    background: linear-gradient(180deg, #4a4a4a 0%, #1b1b1b 24%, var(--panel-black) 40%, #000 100%);
    border-radius: 4px;
    color: var(--text-white); text-align: center;
  }
  .panel-prize { left: 7px; width: 135px; }
  .panel-hand { left: 147px; width: 342px; background: linear-gradient(180deg, #111 0%, #000 100%); }
  .panel-countdown { left: 494px; width: 135px; }

  .panel-label { margin-top: 15px; font-size: 13px; font-weight: 600; letter-spacing: .5px; }
  .panel-value { margin-top: 12px; font-size: 37px; font-weight: 700; letter-spacing: .5px; }

  .card-band {
    position: absolute; left: 0; right: 0; top: 6px; height: 80px;
    background: linear-gradient(90deg, #0a0a0a 0%, #3c3c3c 20%, #cfcfcf 50%, #3c3c3c 80%, #0a0a0a 100%);
    opacity: .55;
  }
  .cards { position: absolute; left: 14px; top: 11px; display: flex; gap: 12px; }
  .card {
    position: relative; width: 53px; height: 69px;
    background: var(--card-white); border: 2px solid var(--card-edge); border-radius: 3px;
    box-shadow: 0 1px 3px rgba(0,0,0,.6);
  }
  .card .rank { position: absolute; left: 4px; top: 1px; font-size: 11px; font-weight: 700; line-height: 1; }
  .card .pip { position: absolute; left: 4px; top: 12px; font-size: 9px; line-height: 1; }
  .card .suit { position: absolute; left: 0; right: 0; top: 18px; text-align: center; font-size: 32px; line-height: 1; }
  .red { color: var(--suit-red); }
  .black { color: var(--suit-black); }

  .caption-strip {
    position: absolute; left: 0; right: 0; bottom: 0; height: 22px;
    background: linear-gradient(180deg, #2a2a2a 0%, #000 100%);
    border-top: 2px solid var(--chrome-mid);
    font-size: 9.5px; font-weight: 700; line-height: 19px; letter-spacing: .3px;
  }
</style>
</head>
<body>
<div class="canvas">
  <div class="chrome title-tab">
    <div class="inner"><span class="title">HIGH HAND BONUS</span></div>
  </div>

  <div class="chrome main-bar">
    <div class="panel panel-prize">
      <div class="panel-label">PRIZE</div>
      <div class="panel-value">$250</div>
    </div>

    <div class="panel panel-hand">
      <div class="card-band"></div>
      <div class="cards">
        <div class="card red"><span class="rank">7</span><span class="pip">♥</span><span class="suit">♥</span></div>
        <div class="card black"><span class="rank">7</span><span class="pip">♠</span><span class="suit">♠</span></div>
        <div class="card black"><span class="rank">5</span><span class="pip">♠</span><span class="suit">♠</span></div>
        <div class="card red"><span class="rank">5</span><span class="pip">♦</span><span class="suit">♦</span></div>
        <div class="card red"><span class="rank">T</span><span class="pip">♦</span><span class="suit">♦</span></div>
      </div>
      <div class="caption-strip">TWO PAIR - TABLE 18 (DAN MILLER)</div>
    </div>

    <div class="panel panel-countdown">
      <div class="panel-label">COUNTDOWN</div>
      <div class="panel-value">1:59</div>
    </div>
  </div>
</div>
</body>
</html>
```